Business card for femtech company

Nothing too elaborate but elegant and geared towards the mother and baby market. Prefer full-bleed with logo (attached) rear.

```html
<!DOCTYPE html>
<html lang="en">
<head>
<meta charset="utf-8">
<title>Nestwell business card</title>
<link href="https://fonts.googleapis.com/css2?family=Open+Sans:wght@400;600;700&display=swap" rel="stylesheet">
<style>
  :root {
    --teal: #4fc1b6;
    --teal-deep: #19a697;
    --teal-light: #6fd0c7;
    --grey: #a4a4a4;
    --ink: #1e1e1e;
    --paper: #ffffff;
    --backdrop: #2a2a2c;
  }
  * { box-sizing: border-box; margin: 0; padding: 0; }
  html, body {
    width: 1200px; height: 780px; overflow: hidden;
    background: var(--backdrop);
    font-family: "Open Sans", Arial, sans-serif;
  }
  .sheet {
    width: 1200px; height: 780px;
    display: flex; align-items: center; justify-content: center; gap: 40px;
  }
  .card {
    width: 540px; height: 310px;
    border-radius: 22px;
    position: relative;
    overflow: hidden;
  }

  /* Front */
  .card-front { background: var(--paper); }
  .brand {
    position: absolute; left: 40px; top: 62px;
    display: flex; flex-direction: column; gap: 10px;
  }
  .brand-dot {
    width: 50px; height: 50px; border-radius: 50%;
    background: var(--teal);
  }
  .brand-name {
    font-size: 38px; font-weight: 400; color: var(--grey);
    letter-spacing: 0.5px; line-height: 1;
    padding-left: 30px;
  }
  .divider {
    position: absolute; left: 236px; top: 56px;
    width: 1px; height: 200px; background: #3a3a3a;
  }
  .details {
    position: absolute; left: 256px; top: 72px; right: 18px;
    color: var(--ink);
  }
  .person-name {
    font-size: 25px; font-weight: 700; line-height: 1.1;
    letter-spacing: 0.3px;
  }
  .person-name .first { color: var(--teal); }
  .person-name .last { color: var(--grey); }
  .person-title { font-size: 14px; font-weight: 600; margin-top: 3px; }
  .address { font-size: 13.5px; line-height: 1.35; margin-top: 10px; }
  .contacts { list-style: none; margin-top: 10px; font-size: 13.5px; line-height: 1.4; }
  .contacts li { display: flex; align-items: center; gap: 7px; }
  .contacts svg { width: 12px; height: 12px; flex: none; }

  /* Back */
  .card-back {
    background: linear-gradient(120deg, var(--teal) 0%, var(--teal) 55%, var(--teal-light) 100%);
  }
  .back-pattern { position: absolute; inset: 0; }
  .back-brand {
    position: absolute; left: 250px; bottom: 52px;
    display: flex; align-items: center; gap: 10px;
  }
  .back-brand .brand-dot { width: 26px; height: 26px; background: var(--paper); }
  .back-brand .brand-name {
    color: var(--paper); font-size: 20px; padding-left: 0;
  }
</style>
</head>
<body>
<main class="sheet">
  <section class="card card-front" aria-label="Card front">
    <div class="brand">
      <span class="brand-dot"></span>
      <span class="brand-name">nestwell</span>
    </div>
    <span class="divider"></span>
    <div class="details">
      <p class="person-name"><span class="first">Mara</span> <span class="last">Lindqvist</span></p>
      <p class="person-title">Managing Director</p>
      <p class="address">Harbour Point, 14 Quay Lane,<br>Riverside, Dublin 4, D04 PX72</p>
      <ul class="contacts">
        <li>
          <svg viewBox="0 0 12 12" aria-hidden="true"><path fill="var(--teal)" d="M2.4 1h2l.8 2.4-1.2.9a6.5 6.5 0 0 0 3.7 3.7l.9-1.2 2.4.8v2c0 .8-.6 1.4-1.4 1.4A9.6 9.6 0 0 1 1 2.4C1 1.6 1.6 1 2.4 1z"/></svg>
          (555) 214-0387
        </li>
        <li>
          <svg viewBox="0 0 12 12" aria-hidden="true"><circle cx="6" cy="6" r="5" fill="none" stroke="var(--teal)" stroke-width="1.4"/><path d="M1 6h10M6 1c-2 2.5-2 7.5 0 10M6 1c2 2.5 2 7.5 0 10" fill="none" stroke="var(--teal)" stroke-width="1"/></svg>
          hello@nestwell.com
        </li>
        <li>
          <svg viewBox="0 0 12 12" aria-hidden="true"><rect x="1" y="2.5" width="10" height="7" rx="1" fill="var(--teal)"/><path d="M1.5 3l4.5 3.5L10.5 3" fill="none" stroke="#fff" stroke-width="1"/></svg>
          www.nestwell.com
        </li>
      </ul>
    </div>
  </section>

  <section class="card card-back" aria-label="Card back">
    <div class="back-pattern" role="img" aria-label="Repeating pattern of the brand symbol in deeper teal across the teal background"></div>
    <div class="back-brand">
      <span class="brand-dot"></span>
      <span class="brand-name">nestwell</span>
    </div>
  </section>
</main>
</body>
</html>
```